Entrepreneur needs a business card design

I need a business card to name my three companies, as well as contact information.
I'm open on design and color and it can be plain or complex. I'm open on colors but I think I prefer something somewhat formal but fun as well.
I'm open on whether the background is plain or has design in it. I don't have company logos.
Target Market(s)
Auto dealers, realtors and property managers
Industry/Entity Type
Business
Contact Information for Business Card
HOLLISTER FAMILY PROPERTIES, LLC
HOLLISTER PUBLISHING, LLC
LOTMASTER CONSULTING, LLC
Ned Hollister
2847 W. Tamarack Ave. #310
Boise, Idaho 83611-2905
208-514-3092
ned@holl5x.example

```html
<!DOCTYPE html>
<html lang="en">
<head>
<meta charset="utf-8">
<title>Ned Hollister Business Card</title>
<link rel="stylesheet" href="https://fonts.googleapis.com/css2?family=Open+Sans:wght@400;700&display=swap">
<style>
  :root {
    --page-bg: #e9eaea;
    --card-slate: #4a5e61;
    --card-slate-deep: #3a4c4f;
    --card-white: #ffffff;
    --ink-slate: #4e6467;
    --ink-light: #ffffff;
  }
  html, body {
    margin: 0;
    padding: 0;
    width: 1200px;
    height: 1000px;
    overflow: hidden;
    background: var(--page-bg);
    font-family: "Open Sans", Verdana, sans-serif;
  }
  .business-card {
    position: absolute;
    left: 75px;
    top: 200px;
    width: 1050px;
    height: 600px;
    background: linear-gradient(160deg, var(--card-slate) 0%, var(--card-slate-deep) 100%);
    box-shadow: 0 10px 30px rgba(0,0,0,0.18);
    overflow: hidden;
  }
  .white-panel {
    position: absolute;
    inset: 0;
  }
  .owner-block {
    position: absolute;
    left: 130px;
    top: 215px;
    width: 290px;
    text-align: right;
    color: var(--ink-slate);
  }
  .owner-name {
    font-size: 36px;
    font-weight: 700;
    margin: 0;
    line-height: 1.1;
    text-align: left;
  }
  .owner-title {
    font-size: 23px;
    margin: 0;
    line-height: 1.2;
  }
  .contact-list {
    position: absolute;
    left: 80px;
    top: 420px;
    color: var(--ink-slate);
    font-size: 26px;
    line-height: 48px;
  }
  .contact-line {
    display: flex;
    align-items: center;
    gap: 12px;
  }
  .contact-line svg { width: 30px; height: 26px; fill: var(--ink-slate); }
  .company-list {
    position: absolute;
    right: 40px;
    top: 75px;
    width: 460px;
    margin: 0;
    padding: 0;
    list-style: none;
    color: var(--ink-light);
    font-weight: 700;
    font-size: 22px;
    line-height: 40px;
    text-align: center;
    white-space: nowrap;
  }
  .address {
    position: absolute;
    right: 60px;
    top: 465px;
    color: var(--ink-light);
    font-size: 26px;
    line-height: 40px;
    text-align: right;
  }
  .address-line { display: flex; align-items: center; justify-content: flex-end; gap: 10px; }
  .address-line svg { width: 30px; height: 34px; }
</style>
</head>
<body>
  <div class="business-card">
    <svg class="white-panel" width="1050" height="600" viewBox="0 0 1050 600" aria-hidden="true">
      <path d="M0 0 H380 C 560 110, 600 380, 330 600 H0 Z" fill="var(--card-white)"/>
    </svg>

    <div class="owner-block">
      <p class="owner-name">Ned Hollister</p>
      <p class="owner-title">Owner</p>
    </div>

    <div class="contact-list">
      <div class="contact-line">
        <svg viewBox="0 0 30 26"><path d="M3 7 C3 3 8 2 15 2 C22 2 27 3 27 7 L27 9 L21 9 L21 6 L9 6 L9 9 L3 9 Z M8 11 H22 L26 23 H4 Z"/><circle cx="15" cy="17" r="3" fill="#fff"/></svg>
        <span>: 208-514-3092</span>
      </div>
      <div class="contact-line">
        <svg viewBox="0 0 30 26"><rect x="2" y="4" width="26" height="18"/><path d="M2 4 L15 15 L28 4" stroke="#fff" stroke-width="2" fill="none"/></svg>
        <span>: ned@holl5x.example</span>
      </div>
    </div>

    <ul class="company-list">
      <li>HOLLISTER FAMILY PROPERTIES, LLC</li>
      <li>HOLLISTER PUBLISHING, LLC</li>
      <li>LOTMASTER CONSULTING, LLC</li>
    </ul>

    <div class="address">
      <div class="address-line">
        <svg viewBox="0 0 30 34"><path d="M15 2 C9 2 5 6 5 11 C5 18 15 26 15 26 C15 26 25 18 25 11 C25 6 21 2 15 2 Z" fill="none" stroke="#fff" stroke-width="2.5"/><circle cx="15" cy="11" r="3.5" fill="#fff"/><path d="M3 24 H10 M20 24 H27 L29 32 H1 Z" fill="none" stroke="#fff" stroke-width="2"/></svg>
        <span>: 2847 W. Tamarack Ave. #310 Boise</span>
      </div>
      <div>Idaho 83611-2905</div>
    </div>
  </div>
</body>
</html>
```